Wedding and event Photography company.

We need a business card design for a photography company based in Singapore named TamKeza. Our core service offering is wedding photojournalism. We would like to see minimalistic designs that use the colour white. The final design should communicate a sense of ease and reliability.

The attached are a couple of visual reference which i found over the web, i hope it will helps.

Project Brief Update (14th July 2014):
- Please refrain from using any images from the website for the design. The laws and regulations over here does not allow me to distribute my client's images. Thanks!

Target Market(s)

Young and middle aged adults aged 24 - 38. With money to spend =D

Industry/Entity Type

Business

Contact Information for Business Card

Name: Dev Lunor
Designation: Head Photographer
Mobile: +65 81749026
Email: jun@tamkeza.example
Website: www.tamkeza.example

Font styles to use
Other font styles liked:
• Baskerville URW

Colors

Designer to choose colors to be used in the design.

Requirements
Must have
• Must include:
• - The brand TamKeza
• - The logo attached
• - Please help to place the brand TamKeza with the logo according to your preferences.
• - Services
• - Wedding Photography
• - Portraiture
• - Photojournalism
Nice to have
• Looking forward to an elegant and simple design. Please see attached examples!
• Please use Serif Fonts
Should not have
• Please refrain from using dark tones for the majority of the design.
• Please refrain from letterpress and embossing.

```html
<!DOCTYPE html>
<html lang="en">
<head>
<meta charset="utf-8">
<title>TamKeza — Business Card</title>
<link rel="stylesheet" href="https://fonts.googleapis.com/css2?family=Libre+Baskerville&family=Crimson+Text&display=swap">
<style>
  :root {
    --backdrop: #d2d2d2;
    --card: #f3f3f3;
    --badge-fill: #ececec;
    --ink: #111111;
    --rule: #8a8a8a;
  }
  html, body {
    margin: 0;
    padding: 0;
    width: 1200px;
    height: 960px;
    overflow: hidden;
    background: var(--backdrop);
  }
  .canvas {
    position: relative;
    width: 1200px;
    height: 960px;
  }
  .card {
    position: absolute;
    width: 600px;
    height: 343px;
    background: var(--card);
  }
  .card--front { left: 314px; top: 113px; }
  .card--back  { left: 311px; top: 472px; }

  .contact-badge {
    position: absolute;
    left: 174px;
    top: 49px;
    width: 254px;
    height: 254px;
  }
  .contact-list {
    position: absolute;
    left: 218px;
    top: 116px;
    width: 166px;
    margin: 0;
    padding: 0;
    list-style: none;
    font-family: "Libre Baskerville", "Baskerville", serif;
    color: var(--ink);
    text-align: center;
  }
  .contact-list li { white-space: nowrap; }
  .contact-name {
    font-size: 14px;
    letter-spacing: 7px;
    padding-bottom: 8px;
    border-bottom: 1px dotted var(--rule);
  }
  .contact-phone {
    font-size: 13px;
    letter-spacing: 3px;
    padding-top: 9px;
  }
  .contact-email {
    font-size: 11.5px;
    letter-spacing: 0.6px;
    padding-top: 4px;
    padding-bottom: 6px;
    border-bottom: 1px dotted var(--rule);
  }
  .contact-web {
    font-size: 11.5px;
    letter-spacing: 0.8px;
    padding-top: 8px;
  }

  .brand {
    position: absolute;
    left: 0;
    top: 96px;
    width: 100%;
    text-align: center;
    font-family: "Crimson Text", "Baskerville", serif;
    color: var(--ink);
  }
  .brand-name {
    display: block;
    font-size: 44px;
    line-height: 1;
  }
  .brand-mark {
    display: block;
    width: 46px;
    height: 46px;
    margin: 28px auto 0;
    border-radius: 50%;
    background: var(--ink);
  }
  .services {
    position: absolute;
    left: 0;
    top: 287px;
    width: 100%;
    margin: 0;
    text-align: center;
    font-family: "Crimson Text", "Baskerville", serif;
    font-size: 17px;
    color: var(--ink);
  }
</style>
</head>
<body>
<main class="canvas">
  <section class="card card--front" aria-label="Card front">
    <svg class="contact-badge" viewBox="0 0 254 254" aria-hidden="true">
      <circle cx="127" cy="127" r="124" fill="var(--badge-fill)" stroke="var(--ink)" stroke-width="5"/>
      <circle cx="127" cy="127" r="117" fill="none" stroke="var(--ink)" stroke-width="0.8"/>
    </svg>
    <ul class="contact-list">
      <li class="contact-name">DEV LUNOR</li>
      <li class="contact-phone">+65 81749026</li>
      <li class="contact-email">jun@tamkeza.example</li>
      <li class="contact-web">www.tamkeza.example</li>
    </ul>
  </section>

  <section class="card card--back" aria-label="Card back">
    <div class="brand">
      <span class="brand-name">TamKeza</span>
      <span class="brand-mark" aria-hidden="true"></span>
    </div>
    <p class="services">Wedding Photography | Portraiture | Photojournalism</p>
  </section>
</main>
</body>
</html>
```